Modernisierter Briefkopf für Dienstleistungsunternehmen im Bereich IT-Sicherheitsberatung & Datenschutz
Zielgruppe
Wir haben folgende Dienstleistungen:
Managed Services, IT-Sicherheitsberatung, Datenschutz, Datenschutzbeauftragter,Schulungen,
Kunden sind hauptsächlich Firmen
Aufgabenstellung
siehe Dateiupload, das KORV-Logo soll natürlich weiterhin vorkommen. Den aktuellen Briefkopf habe ich auch hochgeladen.
Das ganze müsste etwas moderner werden.

```html
<!DOCTYPE html>
<html lang="de">
<head>
<meta charset="utf-8">
<title>KORV Briefkopf und Kuvert</title>
<link href="https://fonts.googleapis.com/css2?family=Roboto+Condensed:wght@400;700&family=Gochi+Hand&display=swap" rel="stylesheet">
<style>
  :root {
    --backdrop: #a2bdb8;
    --paper: #ececec;
    --brand: #217562;
    --brand-dark: #155f4f;
    --ink: #3a3a3a;
    --white: #ffffff;
  }
  * { margin: 0; padding: 0; box-sizing: border-box; }
  html, body { width: 1200px; height: 900px; overflow: hidden; }
  body {
    background: var(--backdrop);
    font-family: "Roboto Condensed", Arial, sans-serif;
    color: var(--ink);
    position: relative;
  }
  .letterhead {
    position: absolute; left: 76px; top: 125px;
    width: 439px; height: 628px;
    background: var(--paper);
    box-shadow: 0 6px 18px rgba(0,0,0,.18);
    overflow: hidden;
  }
  .letterhead > * { position: absolute; }
  .brand-band {
    left: 0; top: 37px; width: 245px; height: 56px;
    background: var(--brand);
    border-radius: 0 5px 5px 0;
  }
  .brand-name {
    left: 24px; top: 18px;
    color: var(--white); font-weight: 700; font-size: 15px; letter-spacing: .5px;
  }
  .brand-owner {
    left: 87px; top: 16px; color: var(--white); line-height: 1.2;
  }
  .brand-owner strong { display: block; font-size: 9.5px; font-weight: 700; }
  .brand-owner span { display: block; font-size: 9.5px; }
  .services { left: 25px; top: 97px; font-size: 4.6px; color: var(--ink); }
  .sender-line { left: 25px; top: 113px; font-size: 5px; color: var(--brand); }
  .tagline {
    left: 255px; top: 50px;
    font-family: "Gochi Hand", cursive; font-size: 14.5px; line-height: 1.1; color: #2b2b2b;
  }
  .tagline span { display: block; }
  .tagline span + span { padding-left: 11px; }
  .contact { left: 326px; top: 116px; font-size: 5.6px; line-height: 7.6px; }
  .contact-name { font-size: 9.5px; font-weight: 700; color: var(--brand); line-height: 10px; }
  .contact-sub { font-size: 5.4px; margin-bottom: 4px; }
  .contact-address { margin-bottom: 4px; }
  .contact-table { display: grid; grid-template-columns: 30px auto; }
  .contact-table dd { color: var(--brand); }
  .fold-mark { left: 4px; width: 8px; height: 0.8px; background: var(--brand); }
  .footer-band { left: 0; bottom: 0; width: 439px; height: 28px; }
  .vat-id { right: 27px; bottom: 8px; font-size: 5px; color: var(--white); }
  .vat-id b { font-weight: 700; }

  .envelope {
    position: absolute; left: 662px; top: 451px;
    width: 454px; height: 274px;
    background: var(--paper);
    box-shadow: 0 4px 14px rgba(0,0,0,.16);
  }
  .envelope-flap {
    position: absolute; left: 0; top: 0; width: 454px; height: 72px;
    border-radius: 22px 22px 0 0;
    background: linear-gradient(180deg, #1e6f5c, #19705d);
  }
</style>
</head>
<body>
  <section class="letterhead" aria-label="Briefbogen">
    <div class="brand-band">
      <div class="brand-name">KORV</div>
      <div class="brand-owner"><strong>JONAS BRENNER</strong><span>EDV-KOMMUNIKATIONSTECHNIK</span></div>
    </div>
    <p class="tagline"><span>Ihr Partner für</span><span>IT- und Telekommunikation</span></p>
    <p class="services">Managed Services • IT-Sicherheitsberatung • Datenschutz • Datenschutzbeauftragter • Schulungen</p>
    <p class="sender-line">KORV • Jonas Brenner • Lindenweg 4 • 12345 Musterstadt</p>

    <address class="contact" style="font-style:normal">
      <div class="contact-name">JONAS BRENNER</div>
      <div class="contact-sub">EDV-KOMMUNIKATIONSTECHNIK</div>
      <div class="contact-address">Lindenweg 4<br>12345 Musterstadt</div>
      <dl class="contact-table">
        <dt>Telefon:</dt><dd>+49 000 123 45 67</dd>
        <dt>Mobil:</dt><dd>+49 000 765 43 21</dd>
        <dt>Fax:</dt><dd>+49 000 123 45 68</dd>
        <dt>E-Mail:</dt><dd>info@korv.example</dd>
        <dt></dt><dd>info@netz-loesung.example</dd>
        <dt>Internet:</dt><dd>www.korv.example</dd>
        <dt></dt><dd>www.netz-loesung.example</dd>
      </dl>
    </address>

    <div class="fold-mark" style="top:222px"></div>
    <div class="fold-mark" style="top:314px;width:4px"></div>
    <div class="fold-mark" style="top:444px"></div>

    <svg class="footer-band" viewBox="0 0 439 28" aria-hidden="true">
      <polygon points="0,17 410,0 439,28 0,28" fill="var(--brand-dark)"/>
    </svg>
    <p class="vat-id">USTID: <b>DE000000000</b></p>
  </section>

  <section class="envelope" aria-label="Briefumschlag">
    <div class="envelope-flap" role="img" aria-label="Grünes geometrisches Sechseck-Muster auf der Umschlagklappe"></div>
  </section>
</body>
</html>
```